New Business Card Design for a Payroll Concierge Company

I need a new business card design that is simple and includes my current information. I am a payroll concierge company that processes payroll for clients who employ household employees and I also manage my client's personal bills, financial records. I want to include my current logo and a logo for an association (PFHKT) I belong too on the front of my business card. I will include both my all my company logo files and the association logo files.

Target Market(s)

People who hire household employees, nannies, home health aides, butlers, maids, etc for wealthy individuals and senior citizens who need help in the home.

Industry/Entity Type

Financial Service

Contact Information for Business Card

Company logo

Name: Martin L. Vellacourt
Managing Director

Office number: 203-555-0148
Business Cell: 203-555-0173

Website: www.tallywagedesk.net
Email: Martin.Vellacourt@tallywagedesk.com

Company address:

17 Heron Lane
Suite 208
Wilton,CT 06412

Font styles to use
Serif
Sans Serif

Colors
3176b5
85cae6
cee9f5
33a6d7
d3d3d3
dbdbdb

Requirements
Must have
• I need to have my company logo and name, phone numbers, website, email, and address on the card. I also want the association logo on the card somewhere but not too big. Small enough to see the logo maybe on the top or bottom corner. Or some where on there card that it doesn't take away the design.
Nice to have
• i like the blue color in my logo, grey, please see must haves business card details.
Should not have
• PLEASE DO NOT USE THE BUSINESS CARD DESIGNS IN THE FILES I UPLOADED. I AM NOT INTERESTED IN THAT DESIGN. ALSO THE ADDRESS AND WEBSITE ARE INCORRECT ON THOSE DESIGNS. PLEASE USE THE UPDATED INFO ON BUSINESS CARD DETAILS

```html
<!DOCTYPE html>
<html lang="en">
<head>
<meta charset="utf-8">
<title>Tally Wage Desk – Business Card</title>
<link rel="stylesheet" href="https://fonts.googleapis.com/css2?family=Open+Sans:wght@400;600;700&display=swap">
<style>
  :root {
    --backdrop: #2b2b2d;
    --card-paper: #f4f4f3;
    --brand-blue: #1468b1;
    --accent-blue: #1a6cb8;
    --band-blue: #8fb0d9;
    --ink-navy: #1d2d44;
    --ink-dark: #1e1e1e;
    --icon-dark: #2a2f3a;
    --white: #ffffff;
    --photo-light: #e9eef5;
    --photo-mid: #aab8cb;
    --photo-dark: #5d6f88;
  }
  * { margin: 0; padding: 0; box-sizing: border-box; }
  html, body {
    width: 1200px; height: 1000px; overflow: hidden;
    background: var(--backdrop);
    font-family: "Open Sans", sans-serif;
  }
  .canvas { position: relative; width: 1200px; height: 1000px; }
  .card {
    position: absolute; left: 316px; width: 576px; height: 347px;
    overflow: hidden; box-shadow: 0 6px 18px rgba(0,0,0,.45);
  }
  .card-front { top: 82px; background: var(--card-paper); }
  .card-back { top: 525px; background: var(--brand-blue); }

  .front-shapes { position: absolute; inset: 0; }
  .holder-name {
    position: absolute; left: 326px; top: 90px;
    font-size: 21px; font-weight: 700; color: var(--ink-navy); letter-spacing: .3px;
  }
  .holder-title {
    position: absolute; left: 364px; top: 136px;
    font-size: 11.5px; color: var(--ink-dark); letter-spacing: 2px;
  }
  .contact-row {
    position: absolute; left: 358px; display: flex; align-items: flex-start; gap: 12px;
    font-size: 15.5px; color: var(--ink-dark); line-height: 19px;
  }
  .contact-row svg { flex: none; }
  .row-cell { top: 212px; align-items: center; }
  .row-address { top: 249px; }

  .company-name {
    position: absolute; left: 0; right: 0; top: 126px; text-align: center;
    font-size: 34px; font-weight: 700; color: var(--white); letter-spacing: 1px;
  }
  .association-name {
    position: absolute; right: 24px; top: 252px;
    font-size: 16px; font-weight: 700; color: var(--white); letter-spacing: .5px;
  }
  .contact-band {
    position: absolute; left: 0; right: 0; bottom: 0; height: 57px;
    background: var(--band-blue);
  }
  .band-item {
    position: absolute; display: flex; align-items: center; gap: 8px;
    font-size: 14px; color: var(--white); line-height: 16px;
  }
  .band-web { left: 21px; top: 18px; }
  .band-office { left: 219px; top: 19px; }
  .band-email { left: 373px; top: 10px; }
  .band-email .email-text { text-align: right; margin-left: 10px; }
</style>
</head>
<body>
<div class="canvas">

  <section class="card card-front">
    <svg class="front-shapes" width="576" height="347" viewBox="0 0 576 347">
      <defs>
        <linearGradient id="photoTone" x1="0" y1="0" x2="1" y2="1">
          <stop offset="0" stop-color="var(--photo-mid)"/>
          <stop offset="0.45" stop-color="var(--photo-light)"/>
          <stop offset="1" stop-color="var(--photo-dark)"/>
        </linearGradient>
      </defs>
      <polygon role="img" aria-label="Photo of a calculator and a pen resting on a printed ledger of figures"
               points="0,0 312,0 267,347 0,347" fill="url(#photoTone)"/>
      <rect x="299" y="82" width="277" height="47" fill="var(--band-blue)"/>
      <polygon points="299,129 354,129 336,169" fill="var(--accent-blue)"/>
    </svg>
    <div class="holder-name">Martin L. Vellacourt</div>
    <div class="holder-title">Managing Director</div>

    <div class="contact-row row-cell">
      <svg width="22" height="22" viewBox="0 0 22 22" aria-hidden="true">
        <circle cx="11" cy="11" r="11" fill="var(--accent-blue)"/>
        <path d="M7.5 5.5l2 2.2-1.1 1.4c.8 1.7 2 2.9 3.6 3.7l1.4-1.1 2.2 2-1.2 1.8c-4.1-.5-7.7-4.1-8.2-8.2z" fill="var(--white)"/>
      </svg>
      <span>203-555-0173</span>
    </div>
    <div class="contact-row row-address">
      <svg width="22" height="22" viewBox="0 0 22 22" aria-hidden="true">
        <circle cx="11" cy="11" r="11" fill="var(--accent-blue)"/>
        <circle cx="11" cy="11" r="6.5" fill="none" stroke="var(--white)" stroke-width="1.3"/>
        <ellipse cx="11" cy="11" rx="3" ry="6.5" fill="none" stroke="var(--white)" stroke-width="1.1"/>
        <line x1="4.5" y1="11" x2="17.5" y2="11" stroke="var(--white)" stroke-width="1.1"/>
      </svg>
      <address style="font-style:normal">17 Heron Lane<br>Suite 208<br>Wilton, CT 06412</address>
    </div>
  </section>

  <section class="card card-back">
    <div class="company-name">TALLY WAGE DESK</div>
    <div class="association-name">PFHKT</div>

    <div class="contact-band">
      <div class="band-item band-web">
        <svg width="19" height="19" viewBox="0 0 22 22" aria-hidden="true">
          <circle cx="11" cy="11" r="11" fill="var(--icon-dark)"/>
          <circle cx="11" cy="11" r="6.5" fill="none" stroke="var(--white)" stroke-width="1.3"/>
          <ellipse cx="11" cy="11" rx="3" ry="6.5" fill="none" stroke="var(--white)" stroke-width="1.1"/>
          <line x1="4.5" y1="11" x2="17.5" y2="11" stroke="var(--white)" stroke-width="1.1"/>
        </svg>
        <span>tallywagedesk.net</span>
      </div>
      <div class="band-item band-office">
        <svg width="19" height="19" viewBox="0 0 22 22" aria-hidden="true">
          <circle cx="11" cy="11" r="11" fill="var(--icon-dark)"/>
          <path d="M7.5 5.5l2 2.2-1.1 1.4c.8 1.7 2 2.9 3.6 3.7l1.4-1.1 2.2 2-1.2 1.8c-4.1-.5-7.7-4.1-8.2-8.2z" fill="var(--white)"/>
        </svg>
        <span>203-555-0148</span>
      </div>
      <div class="band-item band-email">
        <svg width="19" height="19" viewBox="0 0 22 22" aria-hidden="true">
          <circle cx="11" cy="11" r="11" fill="var(--icon-dark)"/>
          <rect x="6" y="7.5" width="10" height="7" fill="var(--white)"/>
          <path d="M6 7.5l5 4 5-4" fill="none" stroke="var(--icon-dark)" stroke-width="1"/>
        </svg>
        <span class="email-text">Martin.Vellacourt@<br>tallywagedesk.com</span>
      </div>
    </div>
  </section>

</div>
</body>
</html>
```